Meridale Freightworks Group - needs a website

Build a simple but professional website for Meridale Freightworks Group.
Web address is www.merfregro.com.au
We have just completed developing a brochure and the contents of the brochure would serve as the web pages.
Web design does not need to deviate far from the brochure and will not include electronic commerce etc at this stage.

Target Market(s)

Privately owned logistics businesses in Australia

Industry/Entity Type

Build

Number of Pages Required

5+ page

Requirements
Must have
• Professional, elegant, ability to upload video in the future, ability to add e-commerce in the future

```html
<!DOCTYPE html>
<html lang="en">
<head>
<meta charset="utf-8">
<title>Meridale Freightworks Group</title>
<link href="https://fonts.googleapis.com/css2?family=Open+Sans:wght@400;600;700;800&display=swap" rel="stylesheet">
<style>
:root{
  --navy:#17386a;
  --navy-dark:#0f2a52;
  --band:#1b4e8c;
  --band-line:#4fb3e8;
  --accent:#2ba6df;
  --text:#2b3a55;
  --row:#e9edf3;
  --white:#fff;
}
*{box-sizing:border-box;margin:0;padding:0}
html,body{width:1200px;height:3557px;overflow:hidden}
body{font-family:"Open Sans",Arial,sans-serif;color:var(--text);background:#fff;position:relative}
section,header,footer,nav{position:relative}
.site-header{height:142px;padding:0 40px}
.brand{position:absolute;left:40px;top:40px;display:flex;align-items:center;gap:14px}
.brand-mark{width:58px;height:58px;background:var(--navy)}
.brand-name{font-weight:700;color:var(--navy);font-size:24px;line-height:1.1;width:260px}
.header-contact{position:absolute;right:40px;top:26px;text-align:right}
.phone{display:flex;align-items:center;gap:12px;font-size:30px;color:var(--navy);font-weight:600;justify-content:flex-end}
.tagline{margin-top:24px;font-size:18px;font-weight:600;color:var(--navy)}
.main-nav{height:48px;background:var(--navy);display:flex;justify-content:space-around;align-items:center;padding:0 40px}
.main-nav a{color:#fff;text-decoration:none;font-size:15px;font-weight:600}
.hero{height:516px;background:linear-gradient(180deg,#8a9099 0%,#b8682e 35%,#6e7580 70%,#2c3e55 100%)}
.hero-form{position:absolute;left:735px;top:45px;width:420px;height:304px;background:rgba(20,55,110,.88);padding:14px 22px}
.hero-form h3{background:var(--navy-dark);color:#fff;font-size:18px;padding:8px 12px;margin:0 -10px 14px}
.field{background:var(--navy-dark);color:#fff;font-size:13px;padding:7px 10px;height:32px}
.field-row{display:grid;grid-template-columns:1fr 1fr;gap:8px;margin-bottom:8px}
.field.message{height:98px}
.send{display:block;margin:14px auto 0;width:200px;background:var(--accent);color:#fff;text-align:center;font-weight:700;font-size:14px;padding:6px}
.hero-caption{position:absolute;left:0;right:0;bottom:0;height:120px;background:rgba(15,42,82,.75);text-align:center;color:#fff;padding-top:22px}
.hero-caption h1{font-size:30px;font-weight:800;white-space:nowrap;line-height:1.25}
.hero-caption p{font-size:18px;margin-top:4px;white-space:nowrap}
.section-title{text-align:center;color:var(--navy);font-weight:800;font-size:28px;line-height:1.4}
.lead{text-align:center;font-size:14.5px;line-height:1.5;padding:0 60px;color:var(--text)}
.solution{height:544px;padding-top:30px}
.solution .lead{margin:10px 0 22px}
.pillar{display:flex;height:94px;margin-bottom:4px}
.pillar-label{width:325px;background:linear-gradient(180deg,#1d4c8a,#0f2a52);display:flex;align-items:center;gap:30px;padding-left:75px;color:#4fc0f0;font-size:18px;font-weight:600;line-height:1.2}
.pillar-icon{width:56px;height:56px;border:2px solid #4fc0f0;display:flex;align-items:center;justify-content:center;flex:none}
.pillar-body{flex:1;background:var(--row);display:flex;flex-direction:column;justify-content:center;padding:0 40px;font-size:13.5px;line-height:1.45}
.challenges{height:498px;background:var(--band);color:#fff;padding-top:30px}
.challenges .section-title{color:var(--band-line)}
.challenges .lead{color:#fff;margin-top:8px}
.subhead{text-align:center;font-weight:800;font-size:16px;margin:24px 0 16px}
.dyn-grid{display:grid;grid-template-columns:repeat(3,345px);gap:14px 20px;justify-content:center}
.dyn-card{height:122px;border:2px solid var(--band-line);display:flex;align-items:center;gap:22px;padding:0 18px;font-size:14px;font-weight:600;line-height:1.4}
.dyn-icon{width:76px;height:70px;flex:none;display:flex;align-items:center;justify-content:center}
.approach{height:676px;padding-top:30px}
.approach .lead{margin-top:6px}
.phases{display:flex;justify-content:center;gap:20px;margin:22px 0 30px}
.phase{width:280px;background:var(--navy);color:#fff;text-align:center;font-weight:700;font-size:17px;padding:8px}
.approach .subhead{color:var(--navy);margin:0 0 12px}
.terms{display:flex;justify-content:center;gap:30px;margin-top:28px}
.term{width:200px;text-align:center;font-size:13px;line-height:1.35;color:var(--navy-dark)}
.term h4{font-size:18px;color:var(--navy);margin:10px 0 4px;white-space:nowrap}
.objectives{height:228px;background:var(--band);color:#fff;text-align:center;padding-top:30px}
.objectives .section-title{color:var(--band-line)}
.objectives .lead{color:#fff;margin-top:8px}
.learn{display:inline-block;margin-top:16px;background:var(--accent);color:#fff;font-weight:700;font-size:15px;padding:8px 28px}
.team{height:408px;padding:30px 60px}
.team .section-title{text-align:left}
.bio{font-size:13px;line-height:1.55;margin-top:12px;width:440px}
.bio ul{list-style:none;margin:4px 0 12px}
.ticks li::before{content:"✓ ";color:var(--accent);font-weight:700}
.carousel{position:absolute;left:540px;top:85px;width:600px;height:290px}
.slide{position:absolute;background:#f1f3f6;box-shadow:0 2px 8px rgba(0,0,0,.2);text-align:center}
.slide.side{top:30px;width:150px;height:170px}
.slide.main{left:200px;top:0;width:200px;height:260px;background:#fff}
.portrait{border-radius:50%;margin:20px auto;background:linear-gradient(#9aa5b5,#5f6d83)}
.slide.side .portrait{width:90px;height:90px}
.slide.main .portrait{width:120px;height:120px;margin-top:30px}
.slide-name{position:absolute;bottom:0;left:0;right:0;background:#c7cfda;font-size:12px;color:#667;padding:6px}
.slide.main .slide-name{background:var(--navy);color:#fff;font-size:18px;left:-30px;right:-30px;padding:10px}
.map{height:250px;background:linear-gradient(135deg,#e8eadf,#dfe3d6 50%,#d2dccb)}
.contact{height:247px;padding-top:24px}
.contact-brand{position:absolute;left:70px;top:90px;display:flex;align-items:center;gap:12px}
.contact-details{position:absolute;top:92px;font-size:15px;line-height:1.45;display:flex;gap:10px}
.follow{position:absolute;right:70px;top:92px;text-align:center;font-size:14px;color:var(--navy)}
.social{display:flex;gap:8px;margin-top:8px;justify-content:center}
.social span{width:16px;height:16px;border-radius:50%;background:var(--navy)}
.copyright{position:absolute;left:70px;right:70px;bottom:14px;border-top:1px solid #ccd;font-size:11px;text-align:center;padding-top:10px;font-weight:600}
</style>
</head>
<body>
<header class="site-header">
  <div class="brand"><div class="brand-mark"></div><div class="brand-name">Meridale Freightworks Group</div></div>
  <div class="header-contact">
    <div class="phone"><svg width="34" height="34" viewBox="0 0 34 34"><circle cx="17" cy="17" r="15" fill="none" stroke="#17386a" stroke-width="2.5"/><path d="M11 9l4 1 1 4-2 2c1 3 3 5 6 6l2-2 4 1 1 4-3 2c-8-1-14-7-15-15z" fill="#17386a"/></svg>07 3100 5820</div>
    <div class="tagline">Scale : Synergy : Value</div>
  </div>
</header>
<nav class="main-nav">
  <a>OUR SOLUTION</a><a>THE CHALLENGES</a><a>OUR APPROACH</a><a>KEY MEMBERSHIP TERMS</a><a>OUR OBJECTIVES</a><a>OUR TEAM</a><a>CONTACT</a>
</nav>
<section class="hero" role="img" aria-label="Photograph of a long warehouse aisle lined with orange pallet racking">
  <form class="hero-form">
    <h3>CONTACT US FOR A FREE CONSULTATION</h3>
    <div class="field-row"><div class="field">First Name</div><div class="field">Last Name</div></div>
    <div class="field-row"><div class="field">Email Address</div><div class="field">Phone Number</div></div>
    <div class="field message">Message</div>
    <div class="send">SEND MESSAGE</div>
  </form>
  <div class="hero-caption">
    <h1>A NEW SOLUTION FOR AUSTRALIAN WAREHOUSE BUSINESS OWNERS.</h1>
    <p>Offering national scale to increase revenues, achieving synergies to reduce costs, and enhancing the value in your business.</p>
  </div>
</section>

<section class="solution">
  <h2 class="section-title">OUR SOLUTION</h2>
  <p class="lead">Meridale Freightworks Group provides a national platform to deliver scale to its members. Through this scale, MFG and its members will secure new business. The value of members' businesses will increase, and members will be presented with multiple options to exit.</p>
  <div class="pillar"><div class="pillar-label"><div class="pillar-icon"><svg width="34" height="34" viewBox="0 0 34 34" stroke="#4fc0f0" stroke-width="3" fill="none"><path d="M3 3l10 10M3 3h8M3 3v8M31 3l-10 10M31 3h-8M31 3v8M3 31l10-10M3 31h8M3 31v-8M31 31l-10-10M31 31h-8M31 31v-8"/></svg></div>SCALE</div>
    <div class="pillar-body"><p>• By leveraging its memberships and national presence, MFG will present as a premium logistics provider within the Australia market - a credible alternative to the large corporates.</p><p>• Initial scale at launch is intended to exceed 100,000m2 with over $50 million in annual turnover</p><p>• MFG provides its members with a national network</p></div></div>
  <div class="pillar"><div class="pillar-label"><div class="pillar-icon"><svg width="34" height="34" viewBox="0 0 34 34" stroke="#4fc0f0" stroke-width="3" fill="none"><path d="M5 18l12-12 12 12M5 30l12-12 12 12"/></svg></div>SYNERGY</div>
    <div class="pillar-body"><p>• MFG will provide a centralised business development function on behalf of its members</p><p>• Where MFG can leverage its scale, it will provide reduced costs to its members</p></div></div>
  <div class="pillar"><div class="pillar-label"><div class="pillar-icon"><svg width="34" height="34" viewBox="0 0 34 34" stroke="#4fc0f0" stroke-width="3" fill="none"><circle cx="17" cy="14" r="10"/><path d="M12 27h10M13 31h8M17 8v12"/></svg></div>VALUE</div>
    <div class="pillar-body"><p>• Members' businesses will increase in value as new work is introduced and customer base is diversified</p><p>• With its scale, the ultimate sale of MFG will be at higher multiple and value than any individual member could independently achieved</p></div></div>
  <div class="pillar"><div class="pillar-label"><div class="pillar-icon"><svg width="34" height="34" viewBox="0 0 34 34" stroke="#4fc0f0" stroke-width="3" fill="none"><path d="M12 4h16v26H12M4 17h16M14 11l6 6-6 6"/></svg></div>POTENTIAL<br>EXIT</div>
    <div class="pillar-body"><p>• For members who wish to sell some or all of their businesses, MFG will offer to acquire part of their business</p><p>• This initial exit will enable owners to "take some cash off the table" and de-risk</p></div></div>
</section>

<section class="challenges">
  <h2 class="section-title">THE CHALLENGES</h2>
  <p class="lead">Australian warehouse business owners are facing unprecedented challenges to diversify their client base, compete for work, with national clients, enhance their profitability and ultimately, exit their business.</p>
  <h3 class="subhead">AUSTRALIAN WAREHOUSE INDUSTRY DYNAMICS</h3>
  <div class="dyn-grid">
    <div class="dyn-card"><div class="dyn-icon" role="img" aria-label="Map outline of Australia"><svg width="70" height="56"><rect width="70" height="56" rx="14" fill="#fff"/></svg></div>Exceptionally fragmented - 1600 businesses across Australia</div>
    <div class="dyn-card"><div class="dyn-icon"><svg width="70" height="64" fill="#fff" stroke="#fff" stroke-width="2"><rect x="27" y="24" width="16" height="14"/><rect x="4" y="4" width="12" height="10"/><rect x="54" y="4" width="12" height="10"/><rect x="4" y="50" width="12" height="10"/><rect x="54" y="50" width="12" height="10"/><path d="M10 14v14h17M60 14v14H43M10 50V38h17M60 50V38H43"/></svg></div>Single site operators - increasing challenge to compete against corporates to secure larger contracts</div>
    <div class="dyn-card"><div class="dyn-icon"><svg width="70" height="50"><path d="M5 45a30 30 0 0 1 60 0z" fill="#fff"/><path d="M35 45L50 18" stroke="#1b4e8c" stroke-width="5"/></svg></div>Accelerating industry consolidation</div>
    <div class="dyn-card"><div class="dyn-icon"><svg width="70" height="64" fill="#fff"><rect x="4" y="10" width="8" height="50"/><rect x="16" y="22" width="8" height="38"/><rect x="28" y="32" width="8" height="28"/><rect x="40" y="42" width="8" height="18"/><path d="M4 4l50 40-2-10 8 14-14-2 8-2z"/></svg></div>Substantial margin pressure - Gross profits falling 3% FY13 to FY15</div>
    <div class="dyn-card"><div class="dyn-icon"><svg width="76" height="60" fill="#fff"><circle cx="20" cy="14" r="9"/><circle cx="56" cy="14" r="9"/><circle cx="38" cy="26" r="9"/><path d="M4 44c0-12 32-12 32 0zM40 44c0-12 32-12 32 0zM20 58c0-14 36-14 36 0z"/></svg></div>High customer concentration risk</div>
    <div class="dyn-card"><div class="dyn-icon"><svg width="76" height="66" fill="none" stroke="#fff" stroke-width="3"><circle cx="22" cy="38" r="18"/><circle cx="54" cy="28" r="16"/><circle cx="48" cy="54" r="10"/><text x="15" y="46" fill="#fff" stroke="none" font-size="22" font-weight="700">$</text><text x="47" y="36" fill="#fff" stroke="none" font-size="20" font-weight="700">$</text></svg></div>Ongoing need to invest in technology to maintain market share</div>
  </div>
</section>

<section class="approach">
  <h2 class="section-title">OUR APPROACH</h2>
  <p class="lead">MFG unique approach enable business owners to join with minimal risk, at low cost while retaining control of their business. MFG's approach is focused on achieving maximum value for the business owners over 3 phases:</p>
  <div class="phases"><div class="phase">National Collective</div><div class="phase">Roll-Up</div><div class="phase">MFG Exit</div></div>
  <h3 class="subhead">KEY MEMBERSHIP TERMS</h3>
  <p class="lead">Meridale Freightworks Group provides a national platform to deliver scale to its members. Through this scale, MFG and its members will secure new business. The value of members' businesses will increase, and members will be presented with multiple options to exit.</p>
  <div class="terms">
    <div class="term"><svg width="72" height="72" viewBox="0 0 80 80" fill="none" stroke="#17386a" stroke-width="6"><path d="M18 26a26 26 0 0 1 46 4M62 54a26 26 0 0 1-46-4"/><path d="M12 16v12h12M68 64V52H56"/><text x="28" y="52" fill="#17386a" stroke="none" font-size="32" font-weight="800">$</text></svg><h4>Fee Structure</h4>MFG membership is primarily success based. Membership includes a low cost annual fee. Success fee paid to MFG based on new work introduced to members.</div>
    <div class="term"><svg width="72" height="72" viewBox="0 0 80 80" fill="#17386a"><path d="M10 14l8-8 22 22-8 8z M40 44l8-8 26 26-8 8z M50 10h14v14L24 64l-8 8-8-8 8-8z"/></svg><h4>Alignment</h4>Standard level of service must be adopted to secure national accounts. Pricing for new work will be pre-agreed with members.</div>
    <div class="term"><svg width="72" height="72" viewBox="0 0 80 80" fill="none" stroke="#17386a" stroke-width="7"><path d="M60 22a28 28 0 1 0 0 36"/><path d="M30 40h40M58 28l12 12-12 12"/></svg><h4>Exit</h4>A pre-agreed process for valuing members' businesses will be applied on entry to Phase 2 - on terms demonstrably better than standalone position. Members who retain equity in MFG will cash-out at the same multiple as the MFG founders.</div>
    <div class="term"><svg width="72" height="72" viewBox="0 0 80 80" fill="#17386a"><circle cx="40" cy="34" r="26"/><circle cx="40" cy="34" r="18" fill="#fff"/><path d="M40 20l4 9 10 1-7 7 2 10-9-5-9 5 2-10-7-7 10-1z"/><path d="M22 54l-8 20 12-4 6 8 6-16zM58 54l8 20-12-4-6 8-6-16z"/></svg><h4>Exclusivity</h4>Members will be offered a degree of exclusivity based on geography and service.</div>
    <div class="term"><svg width="72" height="72" viewBox="0 0 80 80"><path d="M8 42l20 20L72 16" fill="none" stroke="#17386a" stroke-width="12"/></svg><h4>Complete Flexibility</h4>Members have no obligation to progress to Phase 2 (i.e. to sell any of their business)</div>
  </div>
</section>

<section class="objectives">
  <h2 class="section-title">OUR OBJECTIVES</h2>
  <p class="lead">MFG intends to deliver tangible benefits to its members resulting in improved profitability, reduced risk and the achievement of measurably higher value. As such MFG offers significant benefits and clear strategic advantages, while presenting a flexible approach with few obligations on members at entry.</p>
  <span class="learn">LEARN MORE</span>
</section>

<section class="team">
  <h2 class="section-title">OUR TEAM</h2>
  <div class="bio">
    <p><strong>Daniel Hartwell</strong><br>B Eng, MApp Fin, GAICD, FFinsia, CPEng, RPEQ</p>
    <p style="margin-top:12px"><strong>M &amp; A Advisory Expertise:</strong></p>
    <ul><li>• $10B in combined transaction experience</li><li>• Tier-1 level M &amp; A and advisory experience</li><li>• Highly discipline approach to business sales</li></ul>
    <ul class="ticks"><li>25 years' international consulting, advisory experience</li><li>Mergers, acquisitions, and divestment experience</li><li>Large bid management credentials leading bid &gt;$500M</li><li>Responsible manager for Australian Financial Services License</li></ul>
  </div>
  <div class="carousel">
    <svg style="position:absolute;left:0;top:80px" width="20" height="40"><path d="M16 2L4 20l12 18" fill="none" stroke="#aab" stroke-width="2"/></svg>
    <div class="slide side" style="left:40px"><div class="portrait" role="img" aria-label="Team member portrait"></div><div class="slide-name">Peter Lyall</div></div>
    <div class="slide side" style="left:410px"><div class="portrait" role="img" aria-label="Team member portrait"></div><div class="slide-name">Simon Crane</div></div>
    <div class="slide main"><div class="portrait" role="img" aria-label="Portrait of Daniel Hartwell"></div><div class="slide-name">Daniel Hartwell</div></div>
    <svg style="position:absolute;right:0;top:80px" width="20" height="40"><path d="M4 2l12 18L4 38" fill="none" stroke="#aab" stroke-width="2"/></svg>
  </div>
</section>

<div class="map" role="img" aria-label="Street map showing the office location"></div>

<footer class="contact">
  <h2 class="section-title">CONTACT</h2>
  <div class="contact-brand"><div class="brand-mark" style="width:44px;height:44px"></div><div class="brand-name" style="font-size:18px;width:200px">Meridale Freightworks Group</div></div>
  <div class="contact-details" style="left:395px"><svg width="16" height="20" viewBox="0 0 16 20"><path d="M8 0a7 7 0 0 1 7 7c0 5-7 13-7 13S1 12 1 7a7 7 0 0 1 7-7z" fill="#17386a"/><circle cx="8" cy="7" r="2.5" fill="#fff"/></svg><div><strong>120 Harbour Road</strong><br>Kelvin Park<br>Eastbrook<br>Melbourne</div></div>
  <div class="contact-details" style="left:690px;flex-direction:column;gap:18px">
    <div style="display:flex;gap:10px;align-items:center"><svg width="18" height="16"><path d="M2 4h14v10H2z" fill="#17386a"/><rect x="0" y="2" width="18" height="4" fill="#17386a"/></svg>07 3100 5820</div>
    <div style="display:flex;gap:10px;align-items:center"><svg width="18" height="14"><rect width="18" height="14" fill="#17386a"/><path d="M0 0l9 8 9-8" stroke="#fff" fill="none"/></svg>peter.lyall@merfregro.com.au</div>
  </div>
  <div class="follow">Follow Us<div class="social"><span></span><span></span><span></span></div></div>
  <p class="copyright">COPYRIGHT © 2015 MERIDALE FREIGHTWORKS GROUP. ALL RIGHTS RESERVED.</p>
</footer>
</body>
</html>
```